Taomeng business card -we import and distributed Chinese herbal medicine into Australia for prac...

We need a business card for our recently purchased and rebranded company. We are a small family run business - husband and wife team. Our logo is red and black, and we would like the card to be white, with an element of gold in the design (the first cloud in the attached png) which when printed we would like embossed in gold. Our website uses Chinese water colour paintings in the banners (www.taomeng.net.au) so a design that is in harmony with this would be ideal.
side one needs to include:

Target Market(s)

potential customers

Industry/Entity Type

Health And Wellness

Contact Information for Business Card

Side 1
logo,
Edmund Varsk Director
Practitioner Support and Education
0491 722 413
edmund@taomeng.net.au
218 Colbury St, Brellick, NT, 0874

side 2 needs to include:
logo
Priscilla Moult Director
Orders, Accounts and Despatch
0487 530 619
priscilla@taomeng.net.au

Font styles to use
Serif

Colors

Designer to choose colors to be used in the design.

Requirements
Must have
• black, red, gold colours
Nice to have
• we like the font papyrus (mac font)

```html
<!DOCTYPE html>
<html lang="en">
<head>
<meta charset="utf-8">
<title>Taomeng Business Cards</title>
<link href="https://fonts.googleapis.com/css2?family=Lato:wght@400;700&display=swap" rel="stylesheet">
<style>
  :root {
    --backdrop: #2b2b2d;
    --card: #ffffff;
    --navy: #1d2140;
    --red: #e0301e;
    --grey: #4a4a4a;
    --rule: #8a8a8a;
    --gold-light: #f3e39a;
    --gold-mid: #dcbf55;
    --gold-deep: #b08e30;
  }
  * { box-sizing: border-box; margin: 0; padding: 0; }
  html, body { width: 1200px; height: 1108px; overflow: hidden; }
  body {
    background: var(--backdrop);
    font-family: "Lato", Arial, sans-serif;
    display: flex;
    justify-content: center;
    align-items: center;
    gap: 60px;
  }
  .card {
    position: relative;
    width: 400px;
    height: 660px;
    background: var(--card);
    border-radius: 22px;
    overflow: hidden;
    box-shadow: 0 14px 30px rgba(0,0,0,0.45);
  }
  .brand {
    position: absolute;
    top: 120px;
    left: 0; right: 0;
    display: flex;
    justify-content: center;
    align-items: center;
    gap: 16px;
  }
  .brand-square {
    width: 62px;
    height: 130px;
    background: var(--red);
  }
  .brand-name {
    font-weight: 400;
    font-size: 64px;
    line-height: 1.02;
    letter-spacing: 2px;
    color: var(--navy);
    text-transform: uppercase;
  }
  .details {
    position: absolute;
    top: 345px;
    left: 0; right: 0;
    text-align: center;
    color: var(--grey);
    font-size: 18px;
    line-height: 1.35;
  }
  .person {
    font-weight: 700;
    font-size: 21px;
    color: var(--navy);
    text-transform: uppercase;
  }
  .person .role { color: var(--red); font-weight: 400; }
  .rule {
    width: 180px;
    height: 1px;
    background: var(--rule);
    margin: 9px auto 9px;
  }
  .cloud {
    position: absolute;
    left: 40px;
    bottom: 0;
    width: 250px;
    height: 110px;
    border-radius: 55% 45% 0 0 / 80% 70% 0 0;
    background: radial-gradient(ellipse at 40% 60%, var(--gold-light), var(--gold-mid) 55%, var(--gold-deep) 100%);
  }
</style>
</head>
<body>
  <section class="card card-front">
    <div class="brand">
      <span class="brand-square"></span>
      <span class="brand-name">Tao<br>meng</span>
    </div>
    <div class="details">
      <p class="person">Edmund Varsk <span class="role">Director</span></p>
      <p>Practitioner support and Education</p>
      <div class="rule"></div>
      <p>0491 722 413</p>
      <p>edmund@taomeng.net.au</p>
      <div class="rule"></div>
      <p>218 Colbury St, Brellick, NT, 0874</p>
    </div>
    <div class="cloud" role="img" aria-label="Embossed gold Chinese auspicious cloud motif"></div>
  </section>

  <section class="card card-back">
    <div class="brand">
      <span class="brand-square"></span>
      <span class="brand-name">Tao<br>meng</span>
    </div>
    <div class="details">
      <p class="person">Priscilla Moult <span class="role">Director</span></p>
      <p>Orders, Accounts and Despatch</p>
      <div class="rule"></div>
      <p>0487 530 619</p>
      <p>priscilla@taomeng.net.au</p>
      <div class="rule"></div>
      <p>218 Colbury St, Brellick, NT, 0874</p>
    </div>
    <div class="cloud" role="img" aria-label="Embossed gold Chinese auspicious cloud motif"></div>
  </section>
</body>
</html>
```